Business card for femtech company

Nothing too elaborate but elegant and geared towards the mother and baby market. Prefer full-bleed with logo (attached) rear.

```html
<!DOCTYPE html>
<html lang="en">
<head>
<meta charset="utf-8">
<title>mamora business card</title>
<link href="https://fonts.googleapis.com/css2?family=Poppins:wght@400;600&display=swap" rel="stylesheet">
<style>
  :root {
    --stage: #8a8a8a;
    --teal: #57c3b8;
    --teal-deep: #4ab3a8;
    --paper: #ececec;
    --ink-grey: #8c8c8c;
    --blush: #f2a39a;
    --emboss-line: #ffffff;
  }
  html, body {
    margin: 0;
    width: 1200px;
    height: 1000px;
    overflow: hidden;
    background: var(--stage);
    font-family: "Poppins", sans-serif;
  }
  .canvas {
    position: relative;
    width: 1200px;
    height: 1000px;
  }
  .card {
    position: absolute;
    left: 294px;
    width: 613px;
    height: 352px;
    border-radius: 28px;
    overflow: hidden;
  }
  .card--front {
    top: 137px;
    background: var(--teal);
    display: flex;
    align-items: center;
    justify-content: center;
    gap: 14px;
  }
  .front-mark {
    width: 34px;
    height: 34px;
    border-radius: 50%;
    background: var(--teal-deep);
  }
  .front-name {
    font-size: 44px;
    font-weight: 400;
    color: var(--teal-deep);
    letter-spacing: 0.5px;
  }
  .card--back {
    top: 556px;
    background: var(--paper);
  }
  .back-decoration {
    position: absolute;
    left: 320px;
    top: 40px;
  }
  .brand {
    position: absolute;
    left: 78px;
    top: 80px;
    display: flex;
    align-items: center;
    gap: 10px;
  }
  .brand-mark {
    width: 26px;
    height: 26px;
    border-radius: 6px;
    background: var(--teal);
  }
  .brand-name {
    font-size: 28px;
    color: var(--ink-grey);
    line-height: 1;
  }
  .contact {
    position: absolute;
    left: 46px;
    top: 146px;
    width: 240px;
    text-align: center;
  }
  .contact-name {
    margin: 0;
    font-size: 22px;
    font-weight: 600;
    color: var(--teal);
    line-height: 1.2;
  }
  .contact-role {
    margin: 2px 0 0;
    font-size: 12px;
    letter-spacing: 3px;
    color: var(--blush);
  }
  .contact-details {
    margin: 14px 0 0;
    font-size: 17px;
    line-height: 22px;
    color: var(--ink-grey);
  }
</style>
</head>
<body>
  <main class="canvas">
    <section class="card card--front">
      <span class="front-mark"></span>
      <span class="front-name">mamora</span>
    </section>

    <section class="card card--back">
      <svg class="back-decoration" width="360" height="360" viewBox="0 0 360 360" aria-hidden="true">
        <circle cx="180" cy="180" r="170" fill="none" stroke="var(--emboss-line)" stroke-width="2.5"/>
      </svg>

      <div class="brand">
        <span class="brand-mark"></span>
        <span class="brand-name">mamora</span>
      </div>

      <div class="contact">
        <p class="contact-name">Name Surname</p>
        <p class="contact-role">POSITION</p>
        <p class="contact-details">
          (123) 456-890<br>
          info@mamorababy.com<br>
          mamorababy.com
        </p>
      </div>
    </section>
  </main>
</body>
</html>
```